Book Cover for Memoir: Sexual Assault and Traumatic Stress

I need a cover design for a memoir that is a victim's story of a sexual assault. I will need a print-on-demand cover, an eBook cover, and a 3D thumbnail image. The thumbnail and eBook cover will be used immediately, and the POD cover will be used in a few months with the full manuscript is ready. Therefore, I need an artist who is willing to make small adjustments if needed once the page count is set.

I have a image I have purchased that should give you an idea of the desired direction, but you can feel free to use your own images. I have attached some examples of book covers I like. I attached a color palette for fonts.

Overall Look: Fonts should be feminine and thin, but large to stand out. Look should be simple and elegant, and display and overall depressing feeling. There should be enough detail though to make it look professionally put together. Not TOO minimalistic.

I have also attached the Print Harbor templates if you choose to use those. If not, ensure there is an open place for the barcode on the bottom right.

Requirements
Must have
• Title: Beneath Quiet Rain
Subtitle: One Woman's Account of Fear, Guilt & Silence
Author: Dana Ruth Whitford
Audience: Mostly women 18-30
Quote (for the back): "I always thought I'd know how I'd react if I ever was raped. I was wrong. I've been wrong a lot lately."
Summary (back cover): When twenty-seven-year-old Dana Whitford wakes up with a gut-wrenching feeling, she has little memory of the horrifying events that occurred the night before. Days earlier, Dana was a spirited single mom who had abandoned her hometown to raise her daughter in the city and pursue her dreams. In the short months since Dana’s move to Seattle, she became the adored lover of a charismatic lawyer, started a new business, and finally felt life was going her way. So what happened to cause her to break?

In a gripping and heartbreaking narrative, Dana tells the true story of how her life unraveled from the traumatic events that took place that night and why what seems obvious to everyone else is impossible for Dana to believe. Beneath Quiet Rain is a chilling exploration of memory through trauma, trust in humanity, and a captivating story of strength and survival that appeals to the heart of fathers and mothers, sons and daughters, and men and women alike.
Nice to have
• BACK COVER: I'd like to have a photo on the back. This should depict the happy life of the main character before the sexual assault, and should be with her daughter. Or should be a nature scene that starts at the corner and blends into the rest of the cover. I have attached a possible image or you can use something you like.

```html
<!DOCTYPE html>
<html lang="en">
<head>
<meta charset="utf-8">
<title>Beneath Quiet Rain — Cover Spread</title>
<link rel="stylesheet" href="https://fonts.googleapis.com/css2?family=Pinyon+Script&family=Italianno&family=Didact+Gothic&display=swap">
<style>
  :root {
    --page: #ffffff;
    --cover: #3c3c3d;
    --spine-line: #5a5a5c;
    --blush: #ec7d72;
    --blush-deep: #c85a52;
    --ink-light: #f6f4f2;
    --shadow: rgba(0, 0, 0, 0.55);
  }
  html, body {
    margin: 0;
    padding: 0;
    overflow: hidden;
    background: var(--page);
  }
  .canvas {
    position: relative;
    width: 1200px;
    height: 851px;
    overflow: hidden;
    background: var(--page);
  }
  .spread {
    position: absolute;
    left: 43px;
    top: 43px;
    width: 1102px;
    height: 757px;
    background: var(--cover);
  }
  .spine-edge {
    position: absolute;
    top: 0;
    width: 1px;
    height: 100%;
    background: var(--spine-line);
  }
  .spine-edge--left { left: 502px; }
  .spine-edge--right { left: 604px; }

  /* Back cover */
  .back-quote {
    position: absolute;
    left: 10px;
    top: 18px;
    width: 482px;
    margin: 0;
    text-align: center;
    font-family: "Italianno", cursive;
    font-size: 36px;
    line-height: 42px;
    color: var(--blush);
    text-shadow: 1px 1px 1px var(--shadow);
  }
  .back-summary {
    position: absolute;
    left: 21px;
    top: 166px;
    width: 472px;
    margin: 0;
    font-family: "Didact Gothic", sans-serif;
    font-size: 19.5px;
    line-height: 26.5px;
    color: var(--ink-light);
  }

  /* Spine */
  .spine-title {
    position: absolute;
    left: 553px;
    top: 14px;
    transform-origin: 0 0;
    transform: translate(34px, 0) rotate(90deg);
    white-space: nowrap;
    margin: 0;
    font-family: "Pinyon Script", cursive;
    font-weight: 400;
    font-size: 50px;
    line-height: 60px;
    color: var(--blush);
    text-shadow: 1px 1px 2px var(--shadow);
  }
  .spine-author {
    position: absolute;
    left: 525px;
    top: 530px;
    transform-origin: 0 0;
    transform: translate(68px, 0) rotate(90deg);
    white-space: nowrap;
    margin: 0;
    font-family: "Didact Gothic", sans-serif;
    font-size: 32px;
    line-height: 34px;
    color: var(--ink-light);
  }

  /* Front cover */
  .front-title {
    position: absolute;
    left: 604px;
    top: 28px;
    width: 498px;
    margin: 0;
    text-align: center;
    font-family: "Pinyon Script", cursive;
    font-weight: 400;
    font-size: 58px;
    line-height: 80px;
    color: var(--blush);
    text-shadow: 1px 1px 0 var(--blush-deep), 2px 3px 3px var(--shadow);
  }
  .front-photo {
    position: absolute;
    left: 742px;
    top: 168px;
    width: 312px;
    height: 502px;
  }
  .front-author {
    position: absolute;
    left: 604px;
    top: 648px;
    width: 498px;
    margin: 0;
    text-align: center;
    font-family: "Didact Gothic", sans-serif;
    font-size: 33px;
    line-height: 40px;
    color: var(--ink-light);
  }
  .front-subtitle {
    position: absolute;
    left: 604px;
    top: 707px;
    width: 498px;
    margin: 0;
    text-align: center;
    font-family: "Didact Gothic", sans-serif;
    font-size: 20px;
    line-height: 26px;
    color: var(--blush);
  }
</style>
</head>
<body>
<div class="canvas">
  <div class="spread">
    <div class="spine-edge spine-edge--left"></div>
    <div class="spine-edge spine-edge--right"></div>

    <!-- Back cover -->
    <p class="back-quote">I always thought I’d know how I’d react if<br>I ever was raped. I was wrong. I’ve been<br>wrong a lot lately...</p>
    <p class="back-summary">When twenty-seven-year-old Dana Whitford wakes up with a gut-wrenching feeling, she has little memory of the horrifying events that occurred the night before. Days earlier, Dana was a spirited single mum who abandoned her hometown to raise her daughter in the city and pursue her dreams. In the short months since Dana’s move to Seattle, she became the adored lover of a charismatic lawyer, started a new business, and finally felt life was going her way. So what happened to cause her to break? In a gripping and heartbreaking narrative, Dana tells the true story of how her life unraveled from the traumatic events that took place that night and why what seems obvious to everyone else is impossible for Dana to believe. Beneath Quiet Rain is a chilling exploration of memory through trauma, trust in humanity, and captivating story of strength and survival that appeals to the hearts of fathers and mothers, sons and daughters, and men and women alike.</p>

    <!-- Spine -->
    <h2 class="spine-title">Beneath Quiet Rain</h2>
    <p class="spine-author">Dana<br>Ruth Whitford</p>

    <!-- Front cover -->
    <h1 class="front-title">Beneath Quiet Rain</h1>
    <p class="front-author">Dana Ruth Whitford</p>
    <p class="front-subtitle">...one woman’s account of fear, guilt &amp; silence</p>
  </div>

  <svg class="front-photo" viewBox="0 0 340 520" preserveAspectRatio="none" role="img" aria-label="Torn photograph of a young woman lying in water, dark hair floating around her, wrapped in a pale sheet">
    <defs>
      <linearGradient id="photo-upper" x1="0" y1="0" x2="0.4" y2="1">
        <stop offset="0" stop-color="#2f3a6a"/>
        <stop offset="0.35" stop-color="#6d7598"/>
        <stop offset="0.7" stop-color="#d8d0d2"/>
        <stop offset="1" stop-color="#ece0da"/>
      </linearGradient>
      <linearGradient id="photo-lower" x1="0" y1="0" x2="0.3" y2="1">
        <stop offset="0" stop-color="#a9aec4"/>
        <stop offset="0.4" stop-color="#e6dbd6"/>
        <stop offset="1" stop-color="#f4ece6"/>
      </linearGradient>
      <filter id="photo-shadow" x="-10%" y="-10%" width="130%" height="130%">
        <feDropShadow dx="4" dy="5" stdDeviation="4" flood-color="#000" flood-opacity="0.6"/>
      </filter>
    </defs>
    <path filter="url(#photo-shadow)" fill="url(#photo-upper)"
      d="M20,0 L320,6 L318,293 L300,285 L285,292 L262,272 L240,276 L222,262 L200,266 L178,250 L160,254 L140,240 L118,238 L96,222 L72,226 L50,206 L34,208 L18,188 Z"/>
    <path filter="url(#photo-shadow)" fill="url(#photo-lower)"
      d="M16,243 L34,252 L52,250 L70,270 L92,268 L114,286 L138,284 L158,300 L180,298 L204,316 L226,312 L248,328 L270,324 L292,338 L316,334 L314,498 L14,498 Z"/>
  </svg>
</div>
</body>
</html>
```